Survey App for phone users trying a new phone with Dual connectivity

Survey App Brief<br/>Design For an Android Survey App for users' feedback on Call, SMS, Data and Streaming Experience on their Mobile phones.<br/><br/>Purpose of the App<br/>To ensure that the user's experience is not impacted by the network switching between two network on the special mobile phones they newly started using.<br/><br/>App Requirements:<br/>First screen: The registration screen, where the user needs to enter the following:<br/>Name: text box<br/>Phone Number: text box<br/>Group Number : <br/><br/>An information text:<br/>By Registering I agree to participate in the Survey.<br/><br/>Register: Button<br/><br/>Start Screen - Survey screens (next time user open the App this will be the first screen):<br/>We need feedback for 4 indicators:<br/>Call Experience<br/>SMS Experience<br/>Data Experience<br/>Streaming Experience<br/><br/>Each Experience can be in the form of a questionnaire or Satisfied/ Somewhat Satisfied / Extremely Satisfied form with radio buttons or on a scale of 1 to 5. We need to ensure that the format used is very professional.<br/><br/>An optional text box for the user to enter the comment in a free format.<br/><br/>This can be done in 4 different screens or in one single screen if it does not give a clumsy look.<br/><br/>A Send button at the end to submit the Survey.<br/><br/>We need a burger menu at the top left corner of this screen, which when expanded will provide 5 options:<br/>Edit User Profile<br/>Survey interval Timer<br/>FAQ<br/>Exit<br/>About<br/><br/><br/>Please ensure that the app is simple, friendly, lively and professional at the same time so that it ignites an interest in the user to use the app.<br/>Use Logo as appropriate.
Telecommunications
Colors
Designer to choose colors to be used in the design.

```html
<!DOCTYPE html>
<html lang="en">
<head>
<meta charset="utf-8">
<title>Survey App Screens</title>
<link href="https://fonts.googleapis.com/css2?family=Lato:wght@400;700&family=Montserrat:wght@600;700&display=swap" rel="stylesheet">
<style>
:root{
  --sky:#4fb3e3;
  --sky-light:#8fd0f5;
  --sky-pale:#d6eefb;
  --navy:#2a5179;
  --paper:#f4f4f4;
  --ink:#2b2b2b;
  --muted:#555;
  --field:#ffffff;
  --btn:#2d2d2d;
  --r1:#f4332e;--r2:#e3b336;--r3:#f6c21a;--r4:#8fd14a;--r5:#2e8b16;
}
*{box-sizing:border-box;margin:0;padding:0}
html,body{width:684px;height:1200px;overflow:hidden}
body{position:relative;background:var(--sky);font-family:"Lato",sans-serif;color:var(--ink)}
.backdrop{position:absolute;inset:0}
.slot{position:absolute;width:237.5px;height:514px;overflow:hidden;box-shadow:0 6px 18px rgba(0,0,0,.18)}
.screen{position:absolute;left:0;top:0;width:375px;height:812px;background:var(--paper);transform:scale(.6333);transform-origin:0 0;overflow:hidden}
.head-band{position:absolute;left:0;top:0;width:100%;height:170px;background:linear-gradient(180deg,#fff 0,#fff 100px,var(--sky) 100px,var(--sky-light) 170px)}
.foot-band{position:absolute;left:0;bottom:0;width:100%;height:70px;background:linear-gradient(180deg,var(--sky-pale),var(--sky-light))}
.brand{position:absolute;top:24px;left:80px;display:flex;align-items:center;gap:14px}
.brand-dot{width:54px;height:54px;border-radius:50%;background:var(--sky-light)}
.brand-name{font-family:"Montserrat",sans-serif;font-weight:600;font-size:19px;line-height:21px;letter-spacing:2px;color:#6d7a84}
.menu-btn{position:absolute;left:36px;top:38px;width:20px}
.menu-btn span{display:block;height:3px;background:var(--ink);margin-bottom:4px}
.title{position:absolute;top:234px;width:100%;text-align:center;font-family:"Montserrat",sans-serif;font-weight:700;font-size:33px;letter-spacing:1.5px}
.field{position:absolute;left:22px;width:331px;height:52px;background:var(--field);box-shadow:0 1px 4px rgba(0,0,0,.1);display:flex;align-items:center;justify-content:space-between;padding:0 24px;font-size:15px;color:#333}
.field svg{width:14px;height:14px;fill:#aaa}
.agree{position:absolute;left:22px;top:533px;font-size:12.5px;color:var(--muted);display:flex;align-items:center;gap:5px}
.agree i{width:10px;height:10px;border:1px solid #777;display:inline-block}
.register{position:absolute;left:22px;top:585px;width:331px;height:52px;background:var(--btn);color:#fff;font-weight:700;font-size:20px;display:flex;align-items:center;justify-content:center;gap:10px}
.register svg{width:20px;height:20px;fill:none;stroke:#fff;stroke-width:2}
.footer{position:absolute;bottom:22px;width:100%;text-align:center;font-size:14px;color:#444}
.card{position:absolute;left:29px;top:276px;width:317px;height:414px;background:#fff;box-shadow:0 1px 5px rgba(0,0,0,.08);padding:18px 0 0 41px}
.metric{height:101px}
.metric h3{font-family:"Montserrat",sans-serif;font-weight:600;font-size:17px;letter-spacing:.8px;margin-bottom:18px}
.scale{display:flex;gap:13px}
.scale span{width:36px;height:36px;color:#fff;font-size:19px;display:flex;align-items:center;justify-content:center}
.s1{background:var(--r1)}.s2{background:var(--r2)}.s3{background:var(--r3)}.s4{background:var(--r4)}.s5{background:var(--r5)}
.dim{position:absolute;inset:0;background:rgba(70,70,70,.78)}
.menu{position:absolute;left:29px;top:195px;width:317px;height:502px;background:#fff;border-radius:10px;padding:38px 0 0 23px}
.menu li{list-style:none;display:flex;align-items:center;gap:21px;height:92.5px;font-size:20px;font-weight:700;color:#222;white-space:nowrap}
.menu .ico{flex:none;width:60px;height:57px;border-radius:4px;background:var(--sky);display:flex;align-items:center;justify-content:center}
.menu .ico svg{width:30px;height:30px;fill:none;stroke:#fff;stroke-width:2.5}
</style>
</head>
<body>
<svg class="backdrop" viewBox="0 0 684 1200" preserveAspectRatio="none" aria-hidden="true">
  <path d="M0,305 Q260,470 684,470 V1200 H0Z" fill="var(--navy)"/>
</svg>

<div class="slot" style="left:97px;top:70px">
  <div class="screen">
    <div class="head-band" role="img" aria-label="Blue header band"></div>
    <div class="foot-band" role="img" aria-label="Light blue footer band"></div>
    <div class="brand"><span class="brand-dot"></span><span class="brand-name">MERIDIAN<br>TELECOM</span></div>
    <h1 class="title">REGISTRATION</h1>
    <div class="field" style="top:310px">Enter Name<svg viewBox="0 0 16 16"><path d="M11 1l4 4-9 9H2v-4z"/></svg></div>
    <div class="field" style="top:377px">Phone Number<svg viewBox="0 0 16 16"><path d="M3 1l3 3-2 2a9 9 0 006 6l2-2 3 3-2 2C6 15 1 10 1 3z"/></svg></div>
    <div class="field" style="top:443px">Group Number<svg viewBox="0 0 16 16"><circle cx="5" cy="5" r="3"/><circle cx="11" cy="5" r="3"/><path d="M0 15a5 5 0 0110 0zM7 15a5 5 0 019 0z"/></svg></div>
    <p class="agree"><i></i>By Registering I agree to participate in the Survey</p>
    <div class="register"><svg viewBox="0 0 20 20"><path d="M9 3H3v14h14v-6M16 2l2 2-8 8H8v-2z"/></svg>REGISTER</div>
    <p class="footer">© 2020 Meridian Telecom.</p>
  </div>
</div>

<div class="slot" style="left:355px;top:70px">
  <div class="screen">
    <div class="head-band" role="img" aria-label="Blue header band"></div>
    <div class="foot-band" role="img" aria-label="Light blue footer band"></div>
    <div class="brand"><span class="brand-dot"></span><span class="brand-name">MERIDIAN<br>TELECOM</span></div>
    <h1 class="title">REGISTRATION</h1>
    <div class="field" style="top:310px">Enter Name<svg viewBox="0 0 16 16"><path d="M11 1l4 4-9 9H2v-4z"/></svg></div>
    <div class="field" style="top:377px">Phone Number<svg viewBox="0 0 16 16"><path d="M3 1l3 3-2 2a9 9 0 006 6l2-2 3 3-2 2C6 15 1 10 1 3z"/></svg></div>
    <div class="field" style="top:443px">Group Number<svg viewBox="0 0 16 16"><circle cx="5" cy="5" r="3"/><circle cx="11" cy="5" r="3"/><path d="M0 15a5 5 0 0110 0zM7 15a5 5 0 019 0z"/></svg></div>
    <p class="agree"><i></i>By Registering I agree to participate in the Survey</p>
    <div class="register"><svg viewBox="0 0 20 20"><path d="M9 3H3v14h14v-6M16 2l2 2-8 8H8v-2z"/></svg>REGISTER</div>
    <p class="footer">© 2020 Meridian Telecom.</p>
  </div>
</div>

<div class="slot" style="left:92px;top:617px">
  <div class="screen">
    <div class="head-band" role="img" aria-label="Blue header band"></div>
    <div class="foot-band" role="img" aria-label="Light blue footer band"></div>
    <div class="menu-btn"><span></span><span></span><span></span></div>
    <div class="brand" style="left:114px"><span class="brand-dot"></span><span class="brand-name">MERIDIAN<br>TELECOM</span></div>
    <h1 class="title" style="top:214px">SURVEY SCREEN</h1>
    <section class="card">
      <div class="metric"><h3>Call Experience</h3><div class="scale"><span class="s1">1</span><span class="s2">2</span><span class="s3">3</span><span class="s4">4</span><span class="s5">5</span></div></div>
      <div class="metric"><h3>SMS Experience</h3><div class="scale"><span class="s1">1</span><span class="s2">2</span><span class="s3">3</span><span class="s4">4</span><span class="s5">5</span></div></div>
      <div class="metric"><h3>Data Experience</h3><div class="scale"><span class="s1">1</span><span class="s2">2</span><span class="s3">3</span><span class="s4">4</span><span class="s5">5</span></div></div>
      <div class="metric"><h3>Streaming Experience</h3><div class="scale"><span class="s1">1</span><span class="s2">2</span><span class="s3">3</span><span class="s4">4</span><span class="s5">5</span></div></div>
    </section>
    <p class="footer">© 2020 Meridian Telecom.</p>
  </div>
</div>

<div class="slot" style="left:355px;top:617px">
  <div class="screen">
    <div class="head-band" role="img" aria-label="Blue header band"></div>
    <div class="foot-band" role="img" aria-label="Light blue footer band"></div>
    <div class="brand" style="left:114px"><span class="brand-dot"></span><span class="brand-name">MERIDIAN<br>TELECOM</span></div>
    <p class="footer">© 2020 Meridian Telecom.</p>
    <div class="dim"></div>
    <div class="menu-btn"><span style="background:#fff"></span><span style="background:#fff"></span><span style="background:#fff"></span></div>
    <ul class="menu">
      <li><span class="ico"><svg viewBox="0 0 30 30"><path d="M13 5H5v20h20v-8M23 3l4 4-11 11h-4v-4z"/></svg></span>Edit User Profile</li>
      <li><span class="ico"><svg viewBox="0 0 30 30"><circle cx="15" cy="15" r="11"/><path d="M15 8v7h-5"/></svg></span>Survey interval Timer</li>
      <li><span class="ico"><svg viewBox="0 0 30 30"><circle cx="15" cy="15" r="12"/><path d="M11 12a4 4 0 118 0c0 3-4 3-4 6M15 22v1"/></svg></span>FAQ</li>
      <li><span class="ico"><svg viewBox="0 0 30 30"><path d="M12 5H5v20h7M13 15h13M21 9l6 6-6 6"/></svg></span>Exit</li>
      <li><span class="ico"><svg viewBox="0 0 30 30" style="fill:#fff;stroke:none"><circle cx="15" cy="10" r="6"/><path d="M4 27a11 9 0 0122 0z"/></svg></span>About</li>
    </ul>
  </div>
</div>
</body>
</html>
```